Corwick Habitat Web

We just need an update/re-design of our existing web site that would include our new company logo and some new photo's. Our current web site can be viewed at www.corwickhabitat.com.au. We would require something very similar to what we have at the moment in terms of content it should all be the same.
The web site would basically act more as a portfolio than one that would generate more business.
We are after a very modern and simple design and maybe something where we can upload our own project photo's and project descriptions as we complete them.

Industry/Entity Type

It Company

```html
<!DOCTYPE html>
<html lang="en">
<head>
<meta charset="utf-8">
<title>Corwick Habitat — Services</title>
<link rel="stylesheet" href="https://fonts.googleapis.com/css2?family=Open+Sans:wght@300;400;600;700&family=Allura&display=swap">
<style>
  :root {
    --ink: #1d1d1f;
    --ink-soft: rgba(29, 29, 31, 0.92);
    --yellow: #ffd500;
    --yellow-deep: #6b5708;
    --white: #ffffff;
    --logo-grey: #a9a9ab;
    --footer: #222224;
    --social: #2a9fd6;
  }
  * { margin: 0; padding: 0; box-sizing: border-box; }
  html, body { width: 1200px; height: 1000px; overflow: hidden; background: var(--footer); }
  body { font-family: "Open Sans", Arial, sans-serif; color: var(--white); }

  .page { position: relative; width: 1200px; height: 1000px; overflow: hidden; }

  .hero-photo {
    position: absolute; left: 0; top: 0; width: 1200px; height: 948px;
    background:
      linear-gradient(90deg, rgba(220,226,230,0.9) 0%, rgba(180,176,170,0.5) 35%, rgba(150,130,110,0.4) 70%, rgba(90,60,40,0.8) 100%),
      linear-gradient(180deg, #c9ccd0 0%, #b9b3a8 45%, #8d8880 75%, #6f6a66 100%);
  }

  .shapes { position: absolute; left: 0; top: 0; }

  .brand {
    position: absolute; left: 40px; top: 180px; width: 330px; text-align: center;
    font-weight: 300; font-size: 34px; color: var(--logo-grey); letter-spacing: 0.5px;
  }

  .main-nav { position: absolute; top: 122px; left: 615px; display: flex; gap: 28px; }
  .main-nav a { color: var(--white); text-decoration: none; font-size: 16px; }

  .submenu { position: absolute; left: 742px; top: 176px; width: 281px; text-align: center;
    font-size: 11px; font-weight: 700; color: var(--yellow-deep); }
  .submenu li { list-style: none; height: 22px; line-height: 22px; }
  .submenu li.is-active { color: var(--white); }

  .services-title {
    position: absolute; left: 316px; top: 328px;
    font-family: "Allura", cursive; font-size: 82px; color: var(--yellow); line-height: 1;
  }

  .tile-label {
    position: absolute; text-align: center; font-weight: 600; font-size: 16px; line-height: 20px;
    color: var(--white); width: 120px;
  }
  .tile-house { left: 208px; top: 585px; }
  .tile-ceilings { left: 509px; top: 598px; }
  .tile-office { left: 359px; top: 733px; }

  .headline { position: absolute; right: 45px; top: 668px; text-align: right; font-weight: 300; line-height: 1; }
  .headline .line-accent { display: block; font-size: 70px; color: var(--yellow); }
  .headline .line-main { display: block; font-size: 54px; color: var(--white); margin-top: 2px; }

  .tagline { position: absolute; right: 45px; top: 840px; text-align: right; font-weight: 300;
    font-size: 26px; line-height: 34px; color: var(--white); }

  .social { position: absolute; right: 45px; top: 920px; display: flex; gap: 7px; }
  .social span { width: 16px; height: 16px; border-radius: 50%; background: var(--social); }

  .footer-rule { position: absolute; left: 0; top: 944px; width: 617px; height: 4px; background: var(--yellow); }
  .site-footer { position: absolute; left: 0; top: 948px; width: 1200px; height: 52px; background: var(--footer); }
  .copyright { position: absolute; left: 50px; top: 19px; font-size: 11px; font-weight: 600; }
</style>
</head>
<body>
<div class="page">
  <div class="hero-photo" role="img" aria-label="Photograph of a modern office interior with glass partitions, a desk and black chairs"></div>

  <svg class="shapes" width="1200" height="948" viewBox="0 0 1200 948">
    <polygon class="brand-diamond" points="0,205 205,0 410,205 205,410" fill="#1d1d1f"/>
    <polygon class="nav-panel" points="360,130 490,0 790,0 1199,130 565,338" fill="rgba(29,29,31,0.94)"/>

    <polygon class="dropdown" points="742,155 1023,155 882,345" fill="#ffd500"/>
    <clipPath id="dropdown-clip"><polygon points="742,155 1023,155 882,345"/></clipPath>
    <rect class="dropdown-active" x="742" y="197" width="281" height="23" fill="#6b5708" clip-path="url(#dropdown-clip)"/>
    <polygon class="dropdown-pointer" points="866,155 898,155 882,169" fill="#1d1d1f"/>

    <polygon class="services-frame" points="420,215 740,535 420,855 100,535" fill="#1d1d1f"/>
    <polygon class="services-photo" role="img" aria-label="Photograph of an office reception with a lit display wall"
      points="420,250 705,535 420,820 135,535" fill="#8c847c"/>
    <polygon class="services-header" points="420,220 578,392 420,548 262,392" fill="#1d1d1f"/>
    <polygon class="tile" points="268,515 353,600 268,685 183,600" fill="rgba(29,29,31,0.92)"/>
    <polygon class="tile" points="568,530 648,610 568,690 488,610" fill="rgba(29,29,31,0.92)"/>
    <polygon class="tile" points="420,660 508,752 420,840 332,752" fill="rgba(29,29,31,0.92)"/>

    <g class="slider-prev">
      <circle cx="1075" cy="535" r="24" fill="#111"/>
      <path d="M1088 535 H1064 M1073 526 L1064 535 L1073 544" stroke="#fff" stroke-width="4" fill="none" stroke-linecap="round" stroke-linejoin="round"/>
    </g>
    <g class="slider-next">
      <circle cx="1131" cy="535" r="24" fill="#ffd500"/>
      <path d="M1118 535 H1142 M1133 526 L1142 535 L1133 544" stroke="#1d1d1f" stroke-width="4" fill="none" stroke-linecap="round" stroke-linejoin="round"/>
    </g>
  </svg>

  <div class="brand">Corwick Habitat</div>

  <nav class="main-nav">
    <a href="#">Home</a>
    <a href="#">Recent Projects</a>
    <a href="#">Our Services</a>
    <a href="#">Contact Us</a>
  </nav>

  <ul class="submenu">
    <li>CEILINGS</li>
    <li class="is-active">WALLS</li>
    <li>COMPOSITE PANELS</li>
  </ul>

  <div class="services-title">Services</div>
  <div class="tile-label tile-house">HOUSE<br>WALL</div>
  <div class="tile-label tile-ceilings">CEILINGS</div>
  <div class="tile-label tile-office">OFFICE<br>WALLS</div>

  <h1 class="headline">
    <span class="line-accent">CREATIVE</span>
    <span class="line-main">INTERIOR DESIGNS</span>
  </h1>

  <p class="tagline">WE CARE ABOUT OUR CLIENTS<br>&amp; CAN MAKE THEIR LIFE EASIER!</p>

  <div class="social"><span></span><span></span><span></span></div>

  <div class="footer-rule"></div>
  <footer class="site-footer">
    <p class="copyright">Copy Right 2014 All Right Reserved</p>
  </footer>
</div>
</body>
</html>
```